Business Card Design for New Game Studio

We need a business card design. We are a new company developing innovative mobile and platform games.

I would like to see very innovative design thats brings out the company's goal and direction.

My Company's goal and direction is to "Evolve the way of gaming, Bring fun and entertainment to all gamers"

Please do use our company logo which I have attached to be included in the design.

Please put in details for name, title, contacts etc ... be creative !!!

Reason: Company logo redesign. Awaiting it. Thanks

Hi all Please do wait for my updated company logo. Thanks

Reason: Still waiting on new company logo. Thanks all

Hi All Designers .... Sorry for the long wait... Please see the new file for my new company logo uploaded. Waiting to see all your creative design. Cheers

Hi All .... Please do not just mass send a whole bunch of similar designs .... Would like to see quality instead of quantity Cheers

Entertainment

```html
<!DOCTYPE html>
<html lang="en">
<head>
<meta charset="utf-8">
<title>Kinetic Play – Business Card</title>
<link href="https://fonts.googleapis.com/css2?family=Roboto+Condensed:wght@400;700&display=swap" rel="stylesheet">
<style>
  :root {
    --bg: #e9e6e1;
    --card: #1c1d1e;
    --card-pattern: #232425;
    --lime: #c8e11e;
    --white: #f2f2f2;
    --muted: #bfc0c0;
  }
  html, body {
    margin: 0;
    width: 1200px;
    height: 1024px;
    overflow: hidden;
    background: var(--bg);
    font-family: "Roboto Condensed", "Arial Narrow", sans-serif;
  }
  .sheet {
    position: relative;
    width: 1200px;
    height: 1024px;
  }
  .card {
    position: absolute;
    left: 197px;
    width: 806px;
    height: 460px;
    background: var(--card);
    box-shadow: 0 10px 30px rgba(0,0,0,0.25);
    overflow: hidden;
  }
  .card--front { top: 36px; }
  .card--back  { top: 528px; }

  /* front */
  .brand-block {
    position: absolute;
    left: 70px;
    top: 0;
    width: 330px;
    height: 460px;
    display: flex;
    align-items: center;
    gap: 14px;
  }
  .brand-square {
    width: 22px;
    height: 22px;
    background: var(--lime);
    flex: none;
  }
  .brand-name {
    color: var(--lime);
    font-weight: 700;
    font-size: 44px;
    letter-spacing: 0.5px;
    white-space: nowrap;
  }
  .details {
    position: absolute;
    left: 450px;
    top: 70px;
    width: 320px;
  }
  .person-name {
    color: var(--lime);
    font-weight: 700;
    font-size: 30px;
    line-height: 1;
    margin: 0;
    text-transform: uppercase;
  }
  .person-title {
    color: var(--white);
    font-size: 17px;
    margin: 6px 0 34px;
  }
  .contact-list {
    list-style: none;
    margin: 0 0 44px;
    padding: 0;
  }
  .contact-list li {
    display: flex;
    align-items: center;
    gap: 12px;
    color: var(--white);
    font-size: 17px;
    line-height: 27px;
  }
  .contact-list svg {
    width: 15px;
    height: 15px;
    flex: none;
    fill: var(--lime);
  }
  .company-name {
    color: var(--lime);
    font-weight: 700;
    font-size: 19px;
    margin: 0 0 4px;
    text-transform: uppercase;
  }
  .company-address {
    color: var(--white);
    font-size: 17px;
    line-height: 24px;
    margin: 0;
  }

  /* back */
  .back-pattern {
    position: absolute;
    inset: 0;
    background: linear-gradient(135deg, var(--card-pattern), var(--card));
  }
  .back-brand {
    position: absolute;
    inset: 0;
    display: flex;
    align-items: center;
    justify-content: center;
    color: var(--lime);
    font-weight: 700;
    font-size: 34px;
  }
</style>
</head>
<body>
<main class="sheet">
  <section class="card card--front" aria-label="Business card front">
    <div class="brand-block">
      <span class="brand-square"></span>
      <span class="brand-name">Kinetic Play</span>
    </div>
    <div class="details">
      <h1 class="person-name">Jordan Hale</h1>
      <p class="person-title">Director</p>
      <ul class="contact-list">
        <li>
          <svg viewBox="0 0 16 16" aria-hidden="true"><path d="M3 1l3 3-2 2c1 2 3 4 5 5l2-2 3 3-2 3C6 15 1 10 1 3z"/></svg>
          +00 123 456 789
        </li>
        <li>
          <svg viewBox="0 0 16 16" aria-hidden="true"><rect x="4" y="0" width="8" height="16" rx="1.5"/></svg>
          +00 123 456 789
        </li>
        <li>
          <svg viewBox="0 0 16 16" aria-hidden="true"><path d="M0 3h16v10H0z M1 4l7 5 7-5" stroke="#1c1d1e" stroke-width="1"/></svg>
          hello@kineticplay.com
        </li>
        <li>
          <svg viewBox="0 0 16 16" aria-hidden="true"><circle cx="8" cy="8" r="7.5"/></svg>
          www.kineticplay.com
        </li>
      </ul>
      <p class="company-name">Kinetic Play</p>
      <p class="company-address">Unit 4, Harbour Lane,<br>Singapore</p>
    </div>
  </section>

  <section class="card card--back" aria-label="Business card back">
    <div class="back-pattern" role="img" aria-label="Faint repeating brand-mark pattern across the card"></div>
    <div class="back-brand">Kinetic Play</div>
  </section>
</main>
</body>
</html>
```